Lantern Capital Business Card Design Project

We have recently rebranded and would like to design new business cards that incorporate the corporate logo - double sided cards with corporate logo on one side and contact details on the other

Target Market(s)

Sophisticated and high net worth investors and finance industry professionals

Industry/Entity Type

Funds Management

Contact Information for Business Card

The card should prominently feature the company name and logo. Other details will be standard contact details for each staff member - name, address, phone, email, website

Colors
0054AA
0677BA
7BADD7
CADEEF
E8F1F8

Requirements
Must have
• Double-sided design with one side prominently featuring the corporate logo and the other side with all standard contact details

```html
<!DOCTYPE html>
<html lang="en">
<head>
<meta charset="UTF-8">
<title>Lantern Capital Business Cards</title>
<link rel="stylesheet" href="https://fonts.googleapis.com/css2?family=Cinzel:wght@400&family=Crimson+Text:wght@400&display=swap">
<style>
  :root {
    --backdrop: #3d3d3f;
    --navy: #1f4170;
    --paper: #ffffff;
    --silver: #d4d8de;
    --ink-grey: #5b5f66;
    --white: #ffffff;
  }
  * { margin: 0; padding: 0; box-sizing: border-box; }
  html, body { width: 1200px; height: 689px; overflow: hidden; }
  body {
    background: var(--backdrop);
    position: relative;
    font-family: "Crimson Text", Georgia, serif;
  }

  .card { position: absolute; box-shadow: 0 14px 30px rgba(0,0,0,.35); }

  /* Contact side, portrait */
  .card--contact {
    left: 150px; top: 64px;
    width: 320px; height: 560px;
    background: var(--paper);
    color: var(--ink-grey);
    padding: 64px 36px 0 40px;
  }
  .contact__name {
    font-family: "Cinzel", Georgia, serif;
    font-weight: 400;
    font-size: 30px;
    letter-spacing: 1px;
    color: var(--navy);
    line-height: 1.1;
  }
  .contact__role { font-size: 17px; margin-top: 2px; }
  .contact__rule {
    width: 18px; height: 2px; background: var(--navy);
    margin: 18px 0 18px;
  }
  .contact__address { font-size: 16px; line-height: 1.35; }
  .contact__icons { display: flex; gap: 6px; margin: 16px 0 12px; }
  .contact__icons svg { width: 13px; height: 13px; fill: var(--navy); }
  .contact__lines { list-style: none; font-size: 16px; line-height: 1.35; }

  .contact__mark {
    position: absolute;
    right: 30px; bottom: 34px;
    font-family: "Crimson Text", Georgia, serif;
    font-weight: 400;
    font-size: 24px;
    color: var(--navy);
    text-align: right;
    line-height: 1.15;
  }

  /* Logo side, landscape */
  .card--logo {
    left: 560px; top: 182px;
    width: 560px; height: 320px;
    background: var(--navy);
    display: flex; flex-direction: column;
    align-items: center; justify-content: center;
  }
  .logo__name {
    font-family: "Crimson Text", Georgia, serif;
    font-weight: 400;
    font-size: 50px;
    letter-spacing: 0;
    color: var(--silver);
  }
  .logo__site {
    margin-top: 22px;
    font-size: 15px;
    letter-spacing: 4px;
    color: var(--white);
  }
</style>
</head>
<body>

  <section class="card card--contact" aria-label="Contact side">
    <h1 class="contact__name">Daniel Hart</h1>
    <p class="contact__role">Founder &amp; CEO</p>
    <div class="contact__rule"></div>
    <p class="contact__address">4127 Alder Lane<br>Norwalk, CT 06851</p>

    <div class="contact__icons" aria-hidden="true">
      <svg viewBox="0 0 16 16"><path d="M4 1l3 3-2 2c1 2 3 4 5 5l2-2 3 3-2 3C7 14 2 9 1 4z"/></svg>
      <svg viewBox="0 0 16 16"><path d="M4 0h8v16H4zM5 2v11h6V2z"/></svg>
      <svg viewBox="0 0 16 16"><path d="M0 3h16v10H0zM1 4l7 5 7-5z"/></svg>
      <svg viewBox="0 0 16 16"><circle cx="8" cy="8" r="7"/><path d="M1 8h14M8 1v14" stroke="#fff" stroke-width="1" fill="none"/></svg>
    </div>

    <ul class="contact__lines">
      <li>(555) 014-2287</li>
      <li>(555) 014-2287</li>
      <li>info@lanterncapital.com</li>
      <li>lanterncapital.com</li>
    </ul>

    <div class="contact__mark">Lantern<br>Capital</div>
  </section>

  <section class="card card--logo" aria-label="Logo side">
    <div class="logo__name">Lantern Capital</div>
    <div class="logo__site">www.LanternCapital.com</div>
  </section>

</body>
</html>
```